Community Management Cooperative Needs a Postcard Design

This will be the first postcard in a 3 part series to be sent to 2,500 management companies in the United States. Neighborhood & Residents Purchasing Alliance helps management companies and communities save money by combining their buying power to drive down costs on everyday business needs. Their membership in the cooperative also connects with other like minded companies in the industry allowing them to share ideas and best practices with one another so that they may improve their business practices. Visit http://joinvelarta.com for more information about the company.

The purpose of this postcard is to get potential members to visit our website to find out more about the cooperative and hopefully apply to become a member. This postcard should convey a message along the lines of "we want you" or "joining forces". I would like to use bright colors and make it eye catching. Can be things along the lines of (but not limited to) super heroes coming together or a patriotic theme, etc. Postcard does not have to be limited to company color palette but provided for reference.
Updates

Target Market(s)

Independent community management companies in the United States, mostly around metropolitan areas. CEO's of companies are usually male and older, 50+

Industry/Entity Type

Community

Requirements
Must have
• Must incorporate our name, logo, and website into the design with a call to action to visit the website.
• http://joinvelarta.com

```html
<!DOCTYPE html>
<html lang="en">
<head>
<meta charset="utf-8">
<title>Velarta Postcard – We Want You</title>
<link rel="stylesheet" href="https://fonts.googleapis.com/css2?family=Jost:wght@400;500;600;700&family=Open+Sans:wght@400;600;700&display=swap">
<style>
  :root {
    --backdrop: #7b7e80;
    --plum: #6b0f5c;
    --plum-deep: #560a49;
    --plum-light: #7d1a6c;
    --lime: #b6d77a;
    --lime-pale: #d4e9a7;
    --white: #ffffff;
    --ink-light: #ffffff;
  }
  * { box-sizing: border-box; margin: 0; padding: 0; }
  html, body {
    width: 1200px; height: 819px; overflow: hidden;
    background: var(--backdrop);
  }
  .postcard {
    position: absolute; left: 101px; top: 89px;
    width: 997px; height: 641px;
    background: var(--white);
    overflow: hidden;
  }
  .hero {
    position: absolute; left: 0; top: 0; width: 997px; height: 411px;
    background: linear-gradient(90deg, var(--plum-deep) 0%, var(--plum) 40%, var(--plum-light) 100%);
  }
  .hero-photo {
    position: absolute; left: 464px; top: 0; width: 533px; height: 411px;
    background:
      radial-gradient(ellipse 42% 55% at 44% 55%, #b33a45 0%, #7a5f78 35%, rgba(60,55,40,0) 70%),
      linear-gradient(90deg, #3c3a2c 0%, #4a4636 45%, #2e2c22 100%);
  }
  .headline {
    position: absolute; left: 36px; top: 30px;
    font-family: "Jost", sans-serif; font-weight: 700;
    font-size: 62px; line-height: 1; letter-spacing: 1px;
    color: var(--lime-pale);
  }
  .tagline {
    position: absolute; left: 38px; top: 93px;
    font-family: "Jost", sans-serif; font-weight: 600;
    font-size: 19.5px; line-height: 24px; letter-spacing: 0.3px;
    color: var(--ink-light);
  }
  .pill {
    position: absolute;
    font-family: "Jost", sans-serif; font-weight: 600;
    color: var(--plum);
    border-radius: 20px;
    display: flex; align-items: center;
  }
  .pill-what {
    left: 36px; top: 162px; width: 188px; height: 32px;
    background: var(--lime-pale);
    font-size: 21px; padding-left: 14px;
  }
  .about {
    position: absolute; left: 38px; top: 204px; width: 360px;
    font-family: "Open Sans", sans-serif; font-size: 13.6px; line-height: 17.6px;
    color: var(--ink-light);
  }
  .about .accent { color: var(--lime-pale); font-weight: 700; }
  .services-band {
    position: absolute; left: 0; top: 411px; width: 997px; height: 104px;
    background: var(--lime);
  }
  .pill-services {
    left: 36px; top: 398px; width: 281px; height: 41px;
    background: var(--white); border: 3px solid var(--plum);
    font-size: 22px; padding-left: 24px; z-index: 2;
  }
  .services {
    position: absolute; top: 426px; list-style: none;
    font-family: "Jost", sans-serif; font-weight: 600; font-size: 19px; line-height: 27px;
    color: var(--plum);
  }
  .services-left { left: 356px; }
  .services-right { left: 647px; }
  .services li { display: flex; align-items: center; gap: 8px; }
  .services svg { width: 19px; height: 19px; flex: none; }
  .brand {
    position: absolute; left: 67px; top: 535px;
    display: flex; align-items: center; gap: 14px;
  }
  .brand-square { width: 90px; height: 89px; background: var(--plum); }
  .brand-name {
    font-family: "Jost", sans-serif; font-weight: 600;
    font-size: 19px; line-height: 24px; letter-spacing: 2px;
    color: var(--plum);
  }
  .cta {
    position: absolute; left: 527px; top: 541px; width: 402px; text-align: center;
    font-family: "Jost", sans-serif; font-weight: 400; font-size: 19.5px;
    color: var(--plum); letter-spacing: 0.2px;
  }
  .url {
    position: absolute; left: 585px; top: 574px; width: 288px; height: 43px;
    border: 3px solid var(--plum); border-radius: 22px;
    display: flex; align-items: center; justify-content: center;
    font-family: "Jost", sans-serif; font-weight: 400; font-size: 19px;
    color: var(--plum); text-decoration: none; letter-spacing: 0.5px;
  }
  .url strong { font-weight: 700; }
</style>
</head>
<body>
  <main class="postcard">
    <section class="hero">
      <div class="hero-photo" role="img" aria-label="Photo of a man opening his jacket to reveal an American flag shirt"></div>
      <h1 class="headline">WE WANT YOU</h1>
      <p class="tagline">MAKING INDEPENDENT MANAGEMENT<br>COMPANIES STRONGER</p>
      <h2 class="pill pill-what">WHAT WE DO</h2>
      <p class="about"><span class="accent">Velarta</span> was created to bring the power of scale to companies and communities like yours. Our alliance works to enhance the value of all members through peer-to-peer networking, savings on products and services, and support for the entrepreneurial spirit. <span class="accent">By joining forces</span> with other likeminded members you are able to gain access to our PooledReach platform that leverages our memberships collective strength to offer programs and services independent companies and communities likely can’t achieve on their own.</p>
    </section>

    <section class="services-band">
    </section>
    <h2 class="pill pill-services">SERVICES FOR YOU</h2>
    <ul class="services services-left">
      <li><svg viewBox="0 0 20 20"><circle cx="10" cy="10" r="9" fill="none" stroke="#6b0f5c" stroke-width="2"/><path d="M5.5 10.2l3 3 6-6.5" fill="none" stroke="#6b0f5c" stroke-width="2.4"/></svg>Peer-to-Peer Networking</li>
      <li><svg viewBox="0 0 20 20"><circle cx="10" cy="10" r="9" fill="none" stroke="#6b0f5c" stroke-width="2"/><path d="M5.5 10.2l3 3 6-6.5" fill="none" stroke="#6b0f5c" stroke-width="2.4"/></svg>Marketing Toolkit</li>
      <li><svg viewBox="0 0 20 20"><circle cx="10" cy="10" r="9" fill="none" stroke="#6b0f5c" stroke-width="2"/><path d="M5.5 10.2l3 3 6-6.5" fill="none" stroke="#6b0f5c" stroke-width="2.4"/></svg>Social Boost</li>
    </ul>
    <ul class="services services-right">
      <li><svg viewBox="0 0 20 20"><circle cx="10" cy="10" r="9" fill="none" stroke="#6b0f5c" stroke-width="2"/><path d="M5.5 10.2l3 3 6-6.5" fill="none" stroke="#6b0f5c" stroke-width="2.4"/></svg>Reputation Management</li>
      <li><svg viewBox="0 0 20 20"><circle cx="10" cy="10" r="9" fill="none" stroke="#6b0f5c" stroke-width="2"/><path d="M5.5 10.2l3 3 6-6.5" fill="none" stroke="#6b0f5c" stroke-width="2.4"/></svg>Member Savings Consultant</li>
      <li><svg viewBox="0 0 20 20"><circle cx="10" cy="10" r="9" fill="none" stroke="#6b0f5c" stroke-width="2"/><path d="M5.5 10.2l3 3 6-6.5" fill="none" stroke="#6b0f5c" stroke-width="2.4"/></svg>Secure Member Website</li>
    </ul>

    <footer>
      <div class="brand">
        <div class="brand-square"></div>
        <p class="brand-name">NEIGHBORHOOD<br>&amp; RESIDENTS PURCHASING<br>ALLIANCE</p>
      </div>
      <p class="cta">JOIN US NOW TO GET MORE INFORMATION</p>
      <a class="url" href="http://joinvelarta.com">WWW.<strong>JOINVELARTA</strong>.COM</a>
    </footer>
  </main>
</body>
</html>
```